Image Broschüre für Veranstaltungstechnik
Zielgruppe
Veranstaltungstechnik
Aufgabenstellung
Modernes aber seriöses Image Produkt, um per Print Werbung an Firmen in der Region zu versenden.
Ich habe das Format geändert in ein kleines Image Book und das Preisgeld dafür deutlich angehoben :)
Daher wäre die aktuelle Version ein kleines „Buch“ im A5 Format, mir ein paar Seiten. Dazu könnte man mit ein Grunddesign mit 2 Seiten oder so vorstellen und dazu die Information geben, wie viele „einfache“ Seiten dieses dann beinhalten würde. Ich denke so an ca 10/15 Seiten wobei das Design sich nicht grundlegend verändern wird. Die Inhalte werden wir dann natürlich liefern
Das ganze sollte dem professionellen Anspruch einer Mittelständigen bis großen Firma entsprechen, welche in erster Linie die Empfänger dieser Inage Broschüre sein sollen. Ausserdem sollte eine kleine Variante erstellt werden ( nur Titelseite evtl etwas abgeändert ), welche auch an Interessierte Firmen als PDF versendet werden kann.
Webseite: www.mv-buehnenlicht-beispiel.de
Weitere Projekte im Bereich Corporate Design und erstellen von Aktionsflyern für bestimmte Events folgen mit Sicherheit.

```html
<!DOCTYPE html>
<html lang="de">
<head>
<meta charset="utf-8">
<title>MV Bühnenlicht – Imagebroschüre</title>
<link rel="stylesheet" href="https://fonts.googleapis.com/css2?family=Fira+Sans+Condensed:wght@500;600;700&family=Fira+Sans:wght@400;600&display=swap">
<style>
  :root{
    --navy:#3a3e95;
    --navy-deep:#2c2f78;
    --navy-soft:#4a4fa6;
    --accent:#86bfd6;
    --paper:#ffffff;
    --canvas:#eeeef2;
    --ink:#3a3a48;
    --head:"Fira Sans Condensed", "Arial Narrow", sans-serif;
    --body:"Fira Sans", Arial, sans-serif;
  }
  *{box-sizing:border-box;margin:0;padding:0}
  html,body{width:836px;height:1200px;overflow:hidden}
  body{background:var(--canvas);font-family:var(--body);color:var(--ink);
    display:flex;flex-direction:column;align-items:center;justify-content:space-evenly;padding:10px 0}
  .spread-row{display:flex;gap:16px}
  .spread{position:relative;width:400px;height:141px;background:var(--paper);
    box-shadow:0 1px 4px rgba(30,30,60,.25);overflow:hidden}

  /* cover */
  .cover-panel{position:absolute;top:0;bottom:0;background:var(--navy);color:#fff;padding:12px 8px}
  .cover-panel.back{left:0;width:18%}
  .cover-panel.front{right:0;width:18%;background:var(--navy-soft);display:flex;flex-direction:column;justify-content:flex-end;padding-bottom:10px}
  .cover-photo{position:absolute;left:18%;right:18%;top:0;bottom:0;
    background:radial-gradient(ellipse at 50% 40%,#5b8fe0 0%,#1f3f9a 45%,#0b1540 100%)}
  .brand{display:flex;align-items:center;gap:4px;font-family:var(--head);font-weight:700;font-size:10px;color:#fff;letter-spacing:.5px}
  .brand::before{content:"";width:7px;height:7px;border-radius:50%;background:#fff}
  .cover-panel.back .brand{margin-top:40px}
  .company{font-family:var(--head);font-weight:600;font-size:4.2px;line-height:1.3;text-transform:uppercase;margin-top:8px}
  .contact{font-size:2.6px;line-height:1.5;margin-top:6px;opacity:.85}
  .contact.web{font-weight:600;margin-top:5px}
  .tagline{font-family:var(--head);font-weight:600;font-size:4.6px;line-height:1.3;text-transform:uppercase;margin-top:10px}

  /* service */
  .spread.service{background:linear-gradient(135deg,var(--navy-soft),var(--navy-deep));color:#fff}
  .service-intro{position:absolute;left:2.5%;top:8%;width:46%}
  .service-head{font-family:var(--head);font-weight:700;font-size:5.6px;letter-spacing:.2px}
  .service-sub{font-family:var(--head);font-weight:600;font-size:3.4px;letter-spacing:.6px;margin-top:2px}
  .service-cols{display:grid;grid-template-columns:1fr 1fr;gap:8px;margin-top:8px}
  .service-cols p{font-size:2.7px;line-height:1.5;margin-bottom:4px;text-align:justify}
  .service-grid-wrap{position:absolute;left:52%;top:8%;right:2.5%}
  .service-grid{display:grid;grid-template-columns:repeat(3,1fr);column-gap:8px;row-gap:9px;margin-top:8px}
  .service-item .num{font-family:var(--head);font-weight:700;font-size:9px;line-height:1}
  .service-item h3{font-family:var(--head);font-weight:600;font-size:3.4px;letter-spacing:.7px;text-transform:uppercase;margin:2px 0}
  .service-item p{font-size:2.6px;line-height:1.5}

  /* topic pages */
  .edge{position:absolute;left:0;top:0;bottom:0;width:3px;background:var(--navy)}
  .topic .num{position:absolute;left:4.5%;top:6%;font-family:var(--head);font-weight:700;font-size:9px;color:var(--accent);letter-spacing:.5px}
  .topic-title{position:absolute;left:4.2%;bottom:9%;writing-mode:vertical-rl;transform:rotate(180deg);
    font-family:var(--head);font-weight:700;font-size:9.5px;color:var(--navy);text-transform:uppercase;letter-spacing:.3px}
  .topic-text{position:absolute;left:10%;top:6%;bottom:8%;display:grid;gap:6px;font-size:2.7px;line-height:1.55;text-align:justify}
  .topic-text p+p{margin-top:3px}
  .text-wide .topic-text{width:30%;grid-template-columns:1fr 1fr}
  .text-narrow .topic-text{width:13.5%;grid-template-columns:1fr}
  .photo{position:absolute;top:6%;bottom:6%;right:0}
  .text-wide .photo{left:42%}
  .text-narrow .photo{left:26%}
  .band{position:absolute;right:0;width:18.5%;height:6%;background:var(--navy)}
  .band.top{top:0}
  .band.bottom{bottom:0}
  .url{position:absolute;bottom:2%;left:52%;font-size:2.6px;font-weight:600;color:var(--accent)}

  .photo.light{background:radial-gradient(ellipse at 55% 70%,#e8f6ff 0%,#4fb4ec 30%,#0d3d8c 75%,#071a45 100%)}
  .photo.truss{background:linear-gradient(110deg,#6b6f78 0%,#c9ccd2 40%,#8e8a84 70%,#4a4540 100%)}
  .photo.stage{background:radial-gradient(circle at 82% 30%,#ffd26a 0%,#e0621c 18%,#7a2a14 45%,#1d2233 80%)}
  .photo.video{background:linear-gradient(180deg,#0c2f8a 0%,#2a6ae0 45%,#0e1e5c 100%)}
  .photo.fair{background:linear-gradient(90deg,#1a1a1e 0%,#d8d8dc 45%,#6a6a70 100%)}
  .media-collage{position:absolute;left:26%;right:0;top:6%;bottom:6%}
  .media-collage .tile{position:absolute}
  .media-collage .t1{left:0;top:0;width:31%;height:42%;background:linear-gradient(160deg,#4aa3e6,#123a8a)}
  .media-collage .t2{left:35%;top:0;width:29%;height:42%;background:linear-gradient(160deg,#9fc8ea,#2b4f7e)}
  .media-collage .t3{left:68%;top:0;width:32%;height:42%;background:linear-gradient(160deg,#5fb6f0,#1a3f88)}
  .media-collage .t4{left:0;top:30%;width:100%;height:70%;background:linear-gradient(170deg,#2d5fb0 0%,#0f1d3d 55%,#1c1c22 100%)}

  /* references */
  .spread.refs .refs-bg{position:absolute;inset:6% 0 6% 0;background:linear-gradient(100deg,#15183a 0%,#2a1d4a 50%,#8a3a8e 75%,#231440 100%)}
  .refs .band{width:64%;left:18%;right:auto}
  .refs-box{position:absolute;left:2.5%;top:14%;width:45%;bottom:14%;background:#fff;padding:9px 8px;text-align:center}
  .refs-box h2{font-family:var(--head);font-weight:700;font-size:10px;color:var(--accent);letter-spacing:.6px}
  .refs-box p{font-size:2.7px;line-height:1.5;margin:3px auto 0;width:86%}
  .ref-grid{display:grid;grid-template-columns:repeat(6,1fr);gap:7px 8px;margin-top:12px;padding:0 4px}
  .ref-grid span{height:9px;background:#c9cad6;border-radius:1px}
  .refs .url{left:52%;color:var(--accent)}
</style>
</head>
<body>

<article class="spread cover">
  <div class="cover-panel back">
    <p class="brand">M &amp; V</p>
    <p class="company">MV Bühnenlicht<br>GmbH &amp; Co. KG</p>
    <p class="contact">Lindenstraße 8<br>73000 Musterstadt</p>
    <p class="contact">Festnetz: +49 (0)7000-123450<br>Fax: +49 (0)7000-123459</p>
    <p class="contact web">www.mv-buehnenlicht-beispiel.de</p>
  </div>
  <div class="cover-photo" role="img" aria-label="Konzertbühne mit blauen Lichtstrahlen und Publikum"></div>
  <div class="cover-panel front">
    <p class="brand">M &amp; V</p>
    <p class="tagline">Ihr Partner<br>für Medien- / Licht<br>und Tontechnik</p>
  </div>
</article>

<div class="spread-row">
  <article class="spread service">
    <div class="service-intro">
      <h2 class="service-head">BERATUNG | KONZEPTION | TECHNIK</h2>
      <p class="service-sub">– ALLES AUS EINER HAND</p>
      <div class="service-cols">
        <div>
          <p>MV Bühnenlicht ist ein Full-Service Anbieter für Licht-, Ton- und Medientechnik. Seit vielen Jahren begleiten wir Messen, Konzerte, Firmenfeiern und Konferenzen als zuverlässiger Partner – von der ersten Idee bis zum letzten Abbau.</p>
          <p>Unser breites Angebot reicht von Beleuchtung und Beschallung über Videowände bis zu Dolmetscheranlagen. Bei uns steht immer der Service im Vordergrund.</p>
        </div>
        <div>
          <p>Wir planen gemeinsam mit Ihnen jede Veranstaltung vom ersten Gespräch an und bringen unsere langjährige Erfahrung in alle Schritte ein.</p>
          <p>Von unserem Standort in der Region aus betreut ein erfahrenes Team Projekte in ganz Süddeutschland. Gerne beraten wir Sie persönlich.</p>
        </div>
      </div>
    </div>
    <div class="service-grid-wrap">
      <h2 class="service-head">UNSER SERVICE</h2>
      <div class="service-grid">
        <div class="service-item"><p class="num">01.</p><h3>Lichttechnik</h3><p>Moderne Scheinwerfer und Lichteffekte für Bühne, Feier oder Messestand – wir beraten Sie gerne.</p></div>
        <div class="service-item"><p class="num">02.</p><h3>Bühnenaufbau</h3><p>Geschultes Personal baut Ihre Bühne sicher auf und ab – schnell, sauber und termingerecht.</p></div>
        <div class="service-item"><p class="num">03.</p><h3>Medientechnik</h3><p>Aktuelle Medientechnik hebt Sie vom Wettbewerb ab und sorgt für starke Präsentationen.</p></div>
        <div class="service-item"><p class="num">04.</p><h3>Videotechnik</h3><p>Kameras, Leinwände und LED-Wände liefern, installieren und betreuen wir direkt bei Ihnen vor Ort.</p></div>
        <div class="service-item"><p class="num">05.</p><h3>Bühnentechnik</h3><p>Licht, Ton und Bühne aus einer Hand ergeben ein stimmiges Erlebnis für Ihr Publikum.</p></div>
        <div class="service-item"><p class="num">06.</p><h3>Messetechnik</h3><p>Wir zeigen Ihnen die vielen Möglichkeiten moderner Messetechnik – sprechen Sie uns an.</p></div>
      </div>
    </div>
  </article>

  <article class="spread topic text-wide">
    <span class="edge"></span>
    <p class="num">01.</p>
    <h2 class="topic-title">Lichttechnik</h2>
    <div class="topic-text">
      <p>Licht ist ein wichtiges Gestaltungsmittel und erzeugt Atmosphäre. Es setzt Akzente, lenkt Blicke und verwandelt jede nüchterne Halle in einen festlichen Raum. Moderne Scheinwerfer tauchen Ihr Event in jede gewünschte Farbe.</p>
      <p>Unsere Lichtdesigner erstellen für jede Veranstaltung ein eigenes Konzept. Ihr Vorteil: Sie erhalten bestmöglichen Service aus einer Hand und profitieren von vielen Jahren Erfahrung mit großen und kleinen Events.</p>
    </div>
    <div class="photo light" role="img" aria-label="Leere Bühne mit blauen Scheinwerferstrahlen und Nebel"></div>
    <span class="band top"></span><span class="band bottom"></span>
    <p class="url">www.mv-buehnenlicht-beispiel.de</p>
  </article>
</div>

<div class="spread-row">
  <article class="spread topic text-narrow">
    <span class="edge"></span>
    <p class="num">02.</p>
    <h2 class="topic-title">Bühnenaufbau</h2>
    <div class="topic-text">
      <p>Sie planen ein Event und benötigen ein erfahrenes Team für den Bühnenaufbau? Unser geschultes Personal kennt sich mit moderner Bühnentechnik bestens aus und hält jeden Zeitplan ein. Auch bei kleinen Feiern bauen wir Ihre Bühne zuverlässig und in kurzer Zeit auf.</p>
    </div>
    <div class="photo truss" role="img" aria-label="Techniker montiert eine Aluminium-Traverse"></div>
    <span class="band top"></span><span class="band bottom"></span>
    <p class="url">www.mv-buehnenlicht-beispiel.de</p>
  </article>

  <article class="spread topic text-wide">
    <span class="edge"></span>
    <p class="num">05.</p>
    <h2 class="topic-title">Bühnentechnik</h2>
    <div class="topic-text">
      <p>Neben der Sicherheit zählen auch funktionale Faktoren. Bei der Bühnentechnik greifen viele Rädchen ineinander: Licht, Ton und Bühne bilden ein professionelles Ganzes.</p>
      <p>Die Bühnentechnik umfasst mehr als die Bühne selbst. Wir beraten Sie gerne in allen Fragen zur professionellen Bühnentechnik.</p>
    </div>
    <div class="photo stage" role="img" aria-label="Bühne mit Traversen und orangefarbenem Gegenlicht"></div>
    <span class="band top"></span><span class="band bottom"></span>
    <p class="url">www.mv-buehnenlicht-beispiel.de</p>
  </article>
</div>

<div class="spread-row">
  <article class="spread topic text-wide">
    <span class="edge"></span>
    <p class="num">04.</p>
    <h2 class="topic-title">Videotechnik</h2>
    <div class="topic-text">
      <p>Wenn Sie für Ihr Event passende Videotechnik benötigen, sind wir Ihr Ansprechpartner. Wir liefern Projektoren, Leinwände und LED-Wände, bauen sie auf und betreuen sie vor Ort.</p>
      <p>Egal zu welchem Anlass: Wir bieten die passende Videotechnik, damit Ihre Inhalte groß und klar beim Publikum ankommen.</p>
    </div>
    <div class="photo video" role="img" aria-label="Konferenzsaal mit drei Leinwänden und blauer Beleuchtung"></div>
    <span class="band top"></span><span class="band bottom"></span>
    <p class="url">www.mv-buehnenlicht-beispiel.de</p>
  </article>

  <article class="spread topic text-narrow">
    <span class="edge"></span>
    <p class="num">03.</p>
    <h2 class="topic-title">Medientechnik</h2>
    <div class="topic-text">
      <p>Wir sind auf Licht- und Videotechnik spezialisiert. Neben professionellen Kameras und Regietechnik bieten wir große LED-Videowände mit hoher Auflösung. Auch Public Viewings und Großveranstaltungen betreuen wir mit erfahrenem Personal.</p>
    </div>
    <div class="media-collage">
      <div class="tile t1" role="img" aria-label="Monitor einer Lichtsteuerung"></div>
      <div class="tile t2" role="img" aria-label="Fernsehkamera im Studio"></div>
      <div class="tile t3" role="img" aria-label="Bildschirme eines Regieplatzes"></div>
      <div class="tile t4" role="img" aria-label="Mischpult mit Fadern und Tasten"></div>
    </div>
    <span class="band top"></span><span class="band bottom"></span>
    <p class="url">www.mv-buehnenlicht-beispiel.de</p>
  </article>
</div>

<div class="spread-row">
  <article class="spread topic text-wide">
    <span class="edge"></span>
    <p class="num">06.</p>
    <h2 class="topic-title">Messetechnik</h2>
    <div class="topic-text">
      <p>Für Messen braucht es laufend professionelle Technik. Wir liefern Licht, Ton und Medien für Ihren Stand und helfen Ihnen, sich von der Konkurrenz abzuheben.</p>
      <p>Mit der richtigen Beleuchtung wirkt Ihr Stand einladend. Planen Sie Ihren Auftritt mit uns – wir gehen auf alle Wünsche ein.</p>
    </div>
    <div class="photo fair" role="img" aria-label="Messehalle mit Besuchern in Schwarzweiß"></div>
    <span class="band top"></span><span class="band bottom"></span>
    <p class="url">www.mv-buehnenlicht-beispiel.de</p>
  </article>

  <article class="spread refs">
    <div class="refs-bg" role="img" aria-label="Nachts bunt beleuchtetes Schlossgebäude"></div>
    <span class="band top"></span><span class="band bottom"></span>
    <div class="refs-box">
      <h2>REFERENZEN</h2>
      <p>Wir legen höchsten Wert auf Diskretion. Mit vielen Kunden aus Industrie und Kultur verbindet uns eine vertrauensvolle Zusammenarbeit. Hier ein kleiner Auszug.</p>
      <div class="ref-grid" aria-label="Kundenreferenzen">
        <span></span><span></span><span></span><span></span><span></span><span></span>
        <span></span><span></span><span></span><span></span><span></span><span></span>
      </div>
    </div>
    <p class="url">www.mv-buehnenlicht-beispiel.de</p>
  </article>
</div>

</body>
</html>
```